PlumVerse Business Cards

I need a business card designed for PlumVerse. To get an idea of what we do please visit https://brisklayout.example/para-artistas-7

```html
<!DOCTYPE html>
<html lang="en">
<head>
<meta charset="utf-8">
<title>PlumVerse Business Card</title>
<link href="https://fonts.googleapis.com/css2?family=Montserrat:wght@300;400;500&display=swap" rel="stylesheet">
<style>
  :root {
    --backdrop: #2a2a2a;
    --card: #1e1e1e;
    --card-edge: #232323;
    --pattern-dark: #151515;
    --pattern-light: #3a3a3a;
    --accent: #e38f1c;
    --text: #e6e6e6;
    --rule: #8a8a8a;
  }
  * { margin: 0; padding: 0; box-sizing: border-box; }
  html, body { width: 1200px; height: 1138px; overflow: hidden; }
  body {
    background: var(--backdrop);
    font-family: "Montserrat", sans-serif;
    position: relative;
  }
  .card {
    position: absolute;
    border-radius: 16px;
    overflow: hidden;
    background: linear-gradient(160deg, var(--card-edge), var(--card));
  }
  .card-front { left: 274px; top: 186px; width: 624px; height: 376px; }
  .card-back { left: 276px; top: 608px; width: 618px; height: 374px; }

  .front-pattern {
    position: absolute; inset: 0;
    background: linear-gradient(100deg, var(--pattern-dark) 0%, #222 50%, var(--pattern-light) 100%);
  }

  .brand {
    position: absolute; left: 42px; top: 158px;
    display: flex; align-items: center; gap: 22px;
  }
  .brand-dot {
    width: 44px; height: 44px; border-radius: 50%;
    border: 2px solid var(--accent);
  }
  .brand-text { display: flex; flex-direction: column; }
  .brand-name {
    font-weight: 400; font-size: 26px; letter-spacing: 6px;
    color: var(--text); line-height: 1;
  }
  .brand-tagline {
    display: flex; align-items: center; gap: 8px; margin-top: 8px;
    font-size: 7px; letter-spacing: 3px; color: var(--accent);
  }
  .brand-tagline::after {
    content: ""; width: 72px; height: 1px; background: var(--rule);
  }

  .contact { position: absolute; left: 353px; top: 90px; color: var(--text); }
  .contact-name {
    font-weight: 400; font-size: 27px; color: var(--accent); line-height: 1.1;
  }
  .contact-role { font-size: 15px; font-weight: 400; margin-top: 4px; }
  .contact-list { list-style: none; margin-top: 30px; }
  .contact-list li {
    display: flex; align-items: center; gap: 12px;
    font-size: 15px; height: 27px;
  }
  .contact-list svg { width: 14px; height: 14px; fill: var(--accent); flex: none; }
  .contact-address { font-size: 15px; margin-top: 6px; }
</style>
</head>
<body>
  <section class="card card-front">
    <div class="front-pattern" role="img" aria-label="Embossed repeating geometric pattern in black gloss"></div>
  </section>

  <section class="card card-back">
    <div class="brand">
      <span class="brand-dot"></span>
      <div class="brand-text">
        <span class="brand-name">PLUMVERSE</span>
        <span class="brand-tagline">DIGITAL NOTARY</span>
      </div>
    </div>

    <div class="contact">
      <h1 class="contact-name">Wren Halvick</h1>
      <p class="contact-role">President</p>
      <ul class="contact-list">
        <li>
          <svg viewBox="0 0 16 16" aria-hidden="true"><path d="M1 5c0-2 3-3 7-3s7 1 7 3v1h-4V5H5v1H1z M4 7h8l2 7H2z M8 9a2 2 0 1 0 0.01 0z"/></svg>
          000-0000-0000
        </li>
        <li>
          <svg viewBox="0 0 16 16" aria-hidden="true"><path d="M1 3h14v10H1z M2 4l6 5 6-5" stroke="#1e1e1e" stroke-width="1"/></svg>
          wren@plumverse.app
        </li>
        <li>
          <svg viewBox="0 0 16 16" aria-hidden="true"><circle cx="8" cy="8" r="7"/><path d="M1 8h14M8 1v14M3 4h10M3 12h10" stroke="#1e1e1e" stroke-width="1" fill="none"/></svg>
          www.plumverse.app
        </li>
      </ul>
      <p class="contact-address">Larkhaven, Minnesota, US</p>
    </div>
  </section>
</body>
</html>
```